The Wellness Barn Business Card

Info for the front..... (in whichever order and layout looks best)
Carla Penhallow
Physiotherapist
4/37 Upper Creekbank Rd
Tallowbrook
QLD 4712
0462305178
carlapenhallow57@mailbox.example
www.thewellnessbarn.example.au
on the back I would like to be able to write appointments so probably just that heading with lines.
I like a sort of rustic style but mostly professional, colours in naturals, beige, brown, green etc. I dont mind if the logo colour is changed slightly to suit.

```html
<!DOCTYPE html>
<html lang="en">
<head>
<meta charset="utf-8">
<title>The Wellness Barn Business Card</title>
<link href="https://fonts.googleapis.com/css2?family=Open+Sans:wght@400;600;700&display=swap" rel="stylesheet">
<style>
  :root {
    --backdrop: #3a3b3c;
    --card: #ffffff;
    --brand-green: #2d4d1c;
    --ink: #3a3a3a;
    --rule: #4a4a4a;
  }
  * { box-sizing: border-box; margin: 0; padding: 0; }
  html, body {
    width: 1200px; height: 939px; overflow: hidden;
    background: var(--backdrop);
    font-family: "Open Sans", Arial, sans-serif;
  }
  .stage { position: relative; width: 1200px; height: 939px; }
  .card {
    position: absolute;
    width: 560px; height: 320px;
    background: var(--card);
    box-shadow: 0 10px 24px rgba(0,0,0,.45);
  }
  .card-back { left: 70px; top: 70px; }
  .card-front { left: 570px; top: 530px; }

  .brand-name {
    font-family: "Open Sans", Arial, sans-serif;
    font-weight: 700;
    color: var(--brand-green);
    text-align: center;
    line-height: 1.05;
  }
  .card-back .brand-name {
    position: absolute; left: 0; right: 0; top: 48px;
    font-size: 40px;
  }

  .appointment-row {
    position: absolute;
    display: flex; align-items: flex-end; gap: 6px;
    color: var(--brand-green);
    font-weight: 700; font-size: 14px;
  }
  .appointment-row .label { white-space: nowrap; }
  .appointment-row .write-line {
    flex: 1; border-bottom: 2px dotted var(--brand-green); height: 1px; margin-bottom: 4px;
  }
  .row-date { left: 230px; right: 40px; top: 205px; }
  .row-appointments { left: 40px; right: 40px; top: 270px; }

  .card-front .brand-name {
    position: absolute; left: 30px; width: 240px; top: 110px;
    font-size: 36px;
  }
  .divider {
    position: absolute; left: 290px; top: 60px; width: 1px; height: 200px;
    background: var(--rule);
  }
  .contact {
    position: absolute; left: 312px; top: 58px; right: 16px;
    color: var(--ink); font-size: 12.5px; line-height: 1.6;
  }
  .contact .person {
    color: var(--brand-green); font-weight: 700; font-size: 22px; line-height: 1.1;
  }
  .contact .role { margin-bottom: 2px; }
  .contact .address { padding-left: 10px; margin-bottom: 6px; }
  .contact .line { display: flex; align-items: center; gap: 6px; padding-left: 10px; }
  .contact svg { width: 12px; height: 12px; flex: none; fill: var(--brand-green); }
</style>
</head>
<body>
<div class="stage">

  <section class="card card-back">
    <div class="brand-name">The Wellness<br>Barn</div>
    <div class="appointment-row row-date">
      <span class="label">Date:</span><span class="write-line"></span>
      <span class="label">Time:</span><span class="write-line"></span>
    </div>
    <div class="appointment-row row-appointments">
      <span class="label">Appointments:</span><span class="write-line"></span>
    </div>
  </section>

  <section class="card card-front">
    <div class="brand-name">The Wellness<br>Barn</div>
    <div class="divider"></div>
    <div class="contact">
      <div class="person">Carla Penhallow</div>
      <div class="role">Physiotherapist</div>
      <div class="address">
        4/37 Upper Creekbank Rd<br>
        Tallowbrook<br>
        QLD 4712
      </div>
      <div class="line">
        <svg viewBox="0 0 24 24" aria-hidden="true"><path d="M6.6 10.8a15 15 0 0 0 6.6 6.6l2.2-2.2a1 1 0 0 1 1-.25 11.4 11.4 0 0 0 3.6.6 1 1 0 0 1 1 1V20a1 1 0 0 1-1 1A17 17 0 0 1 3 4a1 1 0 0 1 1-1h3.5a1 1 0 0 1 1 1c0 1.25.2 2.45.6 3.6a1 1 0 0 1-.25 1z"/></svg>
        <span>0462305178</span>
      </div>
      <div class="line">
        <svg viewBox="0 0 24 24" aria-hidden="true"><path d="M2 5h20v14H2z M2 5l10 8 10-8" /></svg>
        <span>carlapenhallow57@mailbox.example</span>
      </div>
      <div class="line">
        <svg viewBox="0 0 24 24" aria-hidden="true"><circle cx="12" cy="12" r="10"/></svg>
        <span>www.thewellnessbarn.example.au</span>
      </div>
    </div>
  </section>

</div>
</body>
</html>
```